Design Rum Bottle Label

I want a design for a Rum bottle i want to release.
For now it is planned to call the Rum Kelvoort Dark SpicedRum, like the name of my liqoir store but that is open for change if there is a better proposal.
The design is free, but it should certainly be stylish and radiate that this is a very high-quality product. I attach my logo but it is not a must to process this in the design.

There should be 2 labels, one for the front and one for the back.
what should be included in the front logo:
- Limited edition
- bottle ... / 500 (the bottle number is filled in by hand)
- 38% Vol.
- ℮ 70cl

What should be included on the back logo:
- small symbol recyclable
- small symbol forbidden for pregnant woman
- kelvoort logo (is in attachement)
- in small: produced by 7315 Velvet Lodge

I am adding a photo with the shape of the bottle so that you can take this into account.
The size of the ticket is provided at 9.5cm x 9.5cm.

By entering this competition you agree, if you win, that any minor changes to the design can still be made. If you win, you will receive the agreed amount and in return the design will be delivered in a usable file format in good quality.
By receiving the sum you agree that all rights to this design become the property of ww.kelvoort-example.be and that you may no longer use this design for any other purpose.

```html
<!DOCTYPE html>
<html lang="en">
<head>
<meta charset="utf-8">
<title>Kelvoort Dark Rum – Front and Back Labels</title>
<link rel="stylesheet" href="https://fonts.googleapis.com/css2?family=Almendra:ital,wght@0,400;0,700;1,700&family=Old+Standard+TT&display=swap">
<style>
  :root {
    --page: #f3f3f4;
    --label-green: #1f2b27;
    --copper: #d8a06c;
    --copper-deep: #b98552;
  }
  * { box-sizing: border-box; margin: 0; padding: 0; }
  html, body { width: 900px; height: 1200px; overflow: hidden; }
  body {
    background: var(--page);
    position: relative;
    font-family: "Almendra", serif;
    color: var(--copper);
  }
  .label { position: absolute; }
  .label-shape { position: absolute; inset: 0; width: 100%; height: 100%; }
  .label-content {
    position: absolute; inset: 0;
    display: flex; flex-direction: column; align-items: center;
    text-align: center;
  }

  /* Front label */
  .label--front { left: 80px; top: 625px; width: 292px; height: 322px; }
  .ornament {
    width: 110px; height: 12px; border-radius: 6px;
    background: linear-gradient(90deg, transparent, var(--copper-deep), transparent);
    opacity: .8;
  }
  .ornament--top { margin-top: 58px; }
  .edition { font-size: 18px; line-height: 1; margin: 4px 0 5px; }
  .product-name { font-size: 35px; line-height: 44px; margin-top: 8px; font-weight: 400; }
  .ribbon {
    margin-top: 8px; width: 160px; height: 22px;
    border: 1.5px solid var(--copper); border-radius: 3px;
    display: flex; align-items: center; justify-content: center;
    font-size: 11px; position: relative;
  }
  .ribbon::before, .ribbon::after {
    content: ""; position: absolute; top: 6px; width: 26px; height: 14px;
    border: 1.5px solid var(--copper);
  }
  .ribbon::before { left: -22px; border-right: none; }
  .ribbon::after { right: -22px; border-left: none; }
  .volume { margin-top: 22px; font-size: 13px; display: flex; gap: 6px; align-items: center; }
  .volume .divider { width: 1px; height: 16px; border-left: 1.5px dotted var(--copper); }

  /* Back label */
  .label--back { left: 528px; top: 648px; width: 275px; height: 272px; }
  .brand-mark {
    margin-top: 14px; display: flex; align-items: center; gap: 4px;
    font-size: 11px; letter-spacing: .5px;
  }
  .brand-mark .dot { width: 10px; height: 10px; border: 1.2px solid var(--copper); border-radius: 50%; }
  .brand-shield {
    margin-top: 4px; width: 52px; height: 40px;
    border: 1.5px solid var(--copper); border-radius: 4px 4px 26px 26px;
  }
  .description {
    margin-top: 12px; width: 232px;
    font-family: "Old Standard TT", serif; font-size: 8.6px; line-height: 11.6px;
    text-transform: uppercase; letter-spacing: .2px;
  }
  .produced-by { margin-top: 10px; font-size: 15px; font-weight: 700; font-style: italic; }
  .producer { font-family: "Old Standard TT", serif; font-size: 10px; line-height: 15px; }
  .producer-name { font-size: 11px; margin-top: 3px; }
  .symbols { margin-top: 5px; display: flex; gap: 6px; }
  .symbol { width: 17px; height: 17px; border: 1.3px solid var(--copper); border-radius: 50%; }
</style>
</head>
<body>

<section class="label label--front" aria-label="Front label">
  <svg class="label-shape" viewBox="0 0 300 320" preserveAspectRatio="none" aria-hidden="true">
    <path d="M150 4 C170 4 180 22 200 26 C225 30 240 20 255 38 C262 48 255 60 268 72 C285 88 296 120 296 160 C296 200 285 232 268 248 C255 260 262 272 255 282 C240 300 225 290 200 294 C180 298 170 316 150 316 C130 316 120 298 100 294 C75 290 60 300 45 282 C38 272 45 260 32 248 C15 232 4 200 4 160 C4 120 15 88 32 72 C45 60 38 48 45 38 C60 20 75 30 100 26 C120 22 130 4 150 4Z"
      fill="var(--label-green)" stroke="var(--copper)" stroke-width="3"/>
  </svg>
  <div class="label-content">
    <div class="ornament ornament--top" role="img" aria-label="Scroll flourish ornament"></div>
    <p class="edition">Limited Edition</p>
    <div class="ornament" role="img" aria-label="Scroll flourish ornament"></div>
    <h1 class="product-name">Kelvoort<br>DarkRum</h1>
    <p class="ribbon">Bottle ... / 500</p>
    <p class="volume"><span>℮ 70cl</span><span class="divider"></span><span>38% Vol.</span></p>
  </div>
</section>

<section class="label label--back" aria-label="Back label">
  <svg class="label-shape" viewBox="0 0 300 320" preserveAspectRatio="none" aria-hidden="true">
    <path d="M150 4 C170 4 180 22 200 26 C225 30 240 20 255 38 C262 48 255 60 268 72 C285 88 296 120 296 160 C296 200 285 232 268 248 C255 260 262 272 255 282 C240 300 225 290 200 294 C180 298 170 316 150 316 C130 316 120 298 100 294 C75 290 60 300 45 282 C38 272 45 260 32 248 C15 232 4 200 4 160 C4 120 15 88 32 72 C45 60 38 48 45 38 C60 20 75 30 100 26 C120 22 130 4 150 4Z"
      fill="var(--label-green)" stroke="var(--copper)" stroke-width="3"/>
  </svg>
  <div class="label-content">
    <p class="brand-mark"><span class="dot"></span>Kelvoort</p>
    <div class="brand-shield" role="img" aria-label="Brand crest shape"></div>
    <p class="description">Lorem ipsum dolor sit amet, consectetuer adipiscing elit, sed diam nonummy nibh euismod tincidunt ut laoreet dolore magna aliquam erat volutpat. Ut wisi enim ad minim veniam, quis nostrud exerci tation ullamcorper suscipit lobortis nisl ut aliquip ex ea commodo consequat. Duis</p>
    <p class="produced-by">Produced By</p>
    <p class="producer">7315</p>
    <p class="producer producer-name">Velvet Lodge</p>
    <div class="symbols">
      <span class="symbol" role="img" aria-label="Not for pregnant women symbol"></span>
      <span class="symbol" role="img" aria-label="Recyclable symbol"></span>
    </div>
  </div>
</section>

</body>
</html>
```